Social Media Cover and Profile

We already have our own logo. We just need a fresh design on our social media pages. We are not happy with our current designs. We would like to incorporate our YIKE billboard and the colors are blue (#05143f) and white. You can also incorporate silver as well. We are a family law office (Divorce and Custody) We no longer want to incorporate the Spire of Dunvale photo that we are currently using. You can look at our Facebook page; The Law Office of Miles T. Hadley.

Target Market(s)

Potential Clients

Industry/Entity Type

Family Law

Logo Text

Our Logo Is The Law Office of Miles T. Hadley with the Sheild

Requirements
Must have
• Text to include:
Central Pennslyvania's Premier Family Law Firm

Ability to be resized to and used as all images in social media, including but not limited to: Youtube Channel art, Facebook Cover and Profile.
Nice to have
• Darker color but we are open to "bright" ideas.

```html
<!DOCTYPE html>
<html lang="en">
<head>
<meta charset="utf-8">
<title>Miles T. Hadley – Social Cover</title>
<link rel="stylesheet" href="https://fonts.googleapis.com/css2?family=Marcellus&family=Montserrat:wght@800&display=swap">
<style>
  :root {
    --navy: #05143f;
    --navy-mid: #1b2f73;
    --slate: #4b5478;
    --silver: #b9bcc4;
    --silver-dark: #6e7179;
    --white: #ffffff;
    --mist: #e6e9f3;
    --page: #f4f5f8;
  }
  * { box-sizing: border-box; margin: 0; padding: 0; }
  html, body {
    width: 1200px; height: 1200px; overflow: hidden;
    background: var(--page);
  }
  .canvas {
    width: 1200px; height: 1200px;
    display: flex; align-items: center; justify-content: center;
  }
  .cover {
    width: 1200px; height: 400px;
    display: flex;
    box-shadow: 0 4px 10px rgba(0,0,0,.25);
  }
  .brand-panel {
    width: 450px; height: 100%;
    display: flex; flex-direction: column;
  }
  .brand-header {
    height: 98px; background: var(--white);
    display: flex; align-items: center; justify-content: center; gap: 12px;
  }
  .brand-mark {
    width: 30px; height: 30px; background: var(--navy);
  }
  .brand-name {
    font-family: "Marcellus", serif;
    font-size: 19px; color: var(--navy); letter-spacing: .3px;
  }
  .silver-rule {
    height: 5px;
    background: linear-gradient(90deg, var(--silver-dark), var(--silver), var(--silver-dark));
  }
  .brand-body {
    flex: 1; position: relative;
    background: linear-gradient(180deg, var(--navy-mid) 0%, #2a3568 40%, #1b2a5c 70%, var(--navy) 100%);
    color: var(--white); text-align: center;
    padding-top: 20px;
  }
  .tagline {
    font-family: "Marcellus", serif;
    font-size: 31px; line-height: 1;
  }
  .website {
    margin-top: 26px;
    display: flex; align-items: center; justify-content: center; gap: 10px;
    font-family: "Marcellus", serif; font-size: 22px; letter-spacing: .5px;
  }
  .divider {
    width: 8px;
    background: linear-gradient(90deg, var(--silver-dark), var(--silver), var(--silver-dark));
  }
  .billboard {
    flex: 1; position: relative;
    background: linear-gradient(180deg, #f1f2f8 0%, var(--mist) 55%, #d7dcec 100%);
    display: flex; align-items: center; justify-content: center;
  }
  .billboard-text {
    font-family: "Montserrat", sans-serif; font-weight: 800;
    font-size: 200px; letter-spacing: -4px;
    color: var(--slate);
  }
</style>
</head>
<body>
<main class="canvas">
  <section class="cover">
    <div class="brand-panel">
      <header class="brand-header">
        <span class="brand-mark"></span>
        <span class="brand-name">The Law Office of Miles T. Hadley</span>
      </header>
      <div class="silver-rule"></div>
      <div class="brand-body" role="img" aria-label="Night city skyline reflected in a river, tinted deep blue">
        <h1 class="tagline">Central Pennslyvania's<br>Premier Family Law Firm</h1>
        <p class="website">
          <svg width="24" height="24" viewBox="0 0 24 24" fill="none" stroke="#ffffff" stroke-width="1.6" aria-hidden="true">
            <circle cx="12" cy="12" r="10"/>
            <ellipse cx="12" cy="12" rx="4.5" ry="10"/>
            <line x1="2" y1="12" x2="22" y2="12"/>
            <line x1="4" y1="6.5" x2="20" y2="6.5"/>
            <line x1="4" y1="17.5" x2="20" y2="17.5"/>
          </svg>
          mileshadleylaw.com
        </p>
      </div>
    </div>
    <div class="divider"></div>
    <div class="billboard" role="img" aria-label="Pale misty city skyline with two wedding rings beside the billboard word">
      <span class="billboard-text">YIKE</span>
    </div>
  </section>
</main>
</body>
</html>
```